Publishing company needs book cover for multi-author book

Copperfield Lane Publishing needs a book cover designed for a multi-author book called Harbor Lanterns: Unlikely Triumph Accounts from Remarkable Pioneers. We would like to see designs that incorporates the design theme of the image attached and possibly the image itself. The book will be used by the contributing authors who are  are Healers, Psychics, Coaches, Energy Workers, Astrologers, Numerologist, Tarot Card Readers and will be using this book to both market their business and use in their practices.  The final design should communicate  these spiritual practices.
I would love to see
1. A silhouette or image of a woman holding a ball or circle with the attached art inside of.
2. The concepts in the attached art brought into a  new design or  enhancing the original art.

Target Market(s)
The clients and audiences of the contributing authors
Industry/Entity Type
Spiritual, Body Mind Spirit, Evolving Continuousness, Alternative Healing
Colors
Designer to choose colors to be used in the design.
Requirements
Must have
- Title- Harbor Lanterns: Unlikely Triumph Accounts from Remarkable Pioneers. and the name of the publishing company: Copperfield Lane Publishing

Nice to have
- I would love to have the concept of the artwork coming to life through an image of woman, visionary, healer who is healing the world through her modalities.

Should not have
- Dimensions - 6X9

```html
<!DOCTYPE html>
<html lang="en">
<head>
<meta charset="utf-8">
<title>Harbor Lanterns — Book Cover</title>
<link rel="stylesheet" href="https://fonts.googleapis.com/css2?family=Playfair+Display:wght@400&family=Lato:wght@400&display=swap">
<style>
  :root {
    --night: #0c0610;
    --plum: #2a0c2e;
    --ink: #ffffff;
    --ink-soft: rgba(255,255,255,0.85);
    --orb-blue: #3b6fa8;
    --orb-teal: #4aa0a8;
    --orb-green: #5d7a3a;
    --figure-gold: #e8a24a;
    --figure-violet: #a070e0;
  }
  html, body {
    margin: 0;
    padding: 0;
    overflow: hidden;
    background: var(--night);
  }
  .cover {
    position: relative;
    width: 841px;
    height: 1200px;
    overflow: hidden;
    background:
      radial-gradient(circle at 182px 600px, rgba(255,230,250,0.95) 0, rgba(255,140,220,0.55) 22px, rgba(180,60,160,0.25) 80px, rgba(0,0,0,0) 200px),
      radial-gradient(ellipse 700px 520px at 120px 1180px, rgba(150,40,120,0.75), rgba(0,0,0,0) 70%),
      radial-gradient(ellipse 600px 500px at 700px 1150px, rgba(90,20,90,0.5), rgba(0,0,0,0) 70%),
      linear-gradient(180deg, var(--night) 0%, #140818 45%, var(--plum) 100%);
  }
  .title {
    position: absolute;
    top: 28px;
    left: 0;
    width: 100%;
    margin: 0;
    text-align: center;
    font-family: "Playfair Display", serif;
    font-weight: 400;
    font-size: 138px;
    line-height: 146px;
    letter-spacing: 2px;
    color: var(--ink);
    text-transform: uppercase;
  }
  .title span { display: block; }
  .subtitle {
    position: absolute;
    top: 378px;
    left: 0;
    width: 100%;
    margin: 0;
    text-align: center;
    font-family: "Lato", sans-serif;
    font-weight: 400;
    font-size: 27px;
    letter-spacing: 0.3px;
    color: var(--ink);
  }
  .orb-art {
    position: absolute;
    left: 334px;
    top: 440px;
    width: 650px;
    height: 650px;
    border-radius: 50%;
    background:
      radial-gradient(circle at 45% 40%, #d8e8f0 0, #9cc4d8 12%, var(--orb-teal) 30%, var(--orb-blue) 50%, var(--orb-green) 72%, #22305a 100%);
    box-shadow: 0 0 40px rgba(120,170,230,0.35);
  }
  .figure-art {
    position: absolute;
    left: 0;
    top: 760px;
    width: 300px;
    height: 440px;
    border-radius: 40% 50% 0 0;
    background: linear-gradient(160deg, var(--figure-violet) 0%, #d07ab0 40%, var(--figure-gold) 75%, #b0602a 100%);
    opacity: 0.9;
  }
  .publisher {
    position: absolute;
    left: 300px;
    right: 0;
    bottom: 40px;
    margin: 0;
    text-align: center;
    font-family: "Lato", sans-serif;
    font-weight: 400;
    font-size: 22px;
    letter-spacing: 3px;
    text-transform: uppercase;
    color: var(--ink-soft);
  }
</style>
</head>
<body>
  <main class="cover">
    <h1 class="title"><span>Harbor</span><span>Lanterns</span></h1>
    <p class="subtitle">Unlikely Triumph Accounts from Remarkable Pioneers</p>
    <div class="orb-art" role="img" aria-label="Painted sphere holding a swirling spiral of sky, sea, sun and moon phases"></div>
    <div class="figure-art" role="img" aria-label="Glowing silhouette of a kneeling woman raising her hand toward the sphere"></div>
    <p class="publisher">Copperfield Lane Publishing</p>
  </main>
</body>
</html>
```